依頼詳細
ダイナミックなチラシとポスターをお願いします。
見ただけで「すごい!講演に行ってみたい!!」と思えるような。
記載項目
添付資料のとおり
サイズ
A2ポスターとA4チラシ
ページ数
片面
希望イメージ
シンプル 複雑
単色 カラフル
暗い 明るい
日常 高級
遊び心 厳粛
未来的 伝統的
女性的 男性的
納品ファイル
• 高解像度JPG (.jpg)
• イラストレーター形式 (.ai)
補足説明
開催内容の資料を送ります。
また、講師のプロフィールを送ります。

クレジットは、写真提供:森川拓事務所もしくは(c)Taku Morikawa Office等とご表記ください。
皆様お世話になっております。

ポスターの写真は、スポンサーの関係で前回添付した画像以外は基本的には、使用ができませんのでご了承ください。
そのほかの写真を使いたい場合は、一度こちらに確認いただきます様よろしくお願いします。
皆様いつもお世話になっております。
画像が添付されておりませんでした。大変失礼しました。

ご対応どうぞよろしくお願いします。
左上にPRVマークをつけていただきます様よろしくお願いします。
なお、空白とマークの位置はデータのバランスを維持していただきます様お願いします。
■ 選んだ理由

全体の色合いも非常によかったです。ダイナミックな雰囲気と仲間の絆のイメージをうまく表現していただけたと思います。

■ 提案者全員のお礼・コメント

皆様、たくさんのご応募ありがとうございました。こちらのイメージをうまく呼んでいただいたかと思います。
次回もどうぞよろしくお願いします。

```html
<!DOCTYPE html>
<html lang="ja">
<head>
<meta charset="utf-8">
<title>森川拓講演会 仲間の絆</title>
<link rel="stylesheet" href="https://fonts.googleapis.com/css2?family=Noto+Sans+JP:wght@400;700;900&family=Noto+Serif+JP:wght@500;700;900&family=Yuji+Mai&display=swap">
<style>
:root{
  --sky-top:#0b3f8f;
  --sky-mid:#2f78c8;
  --snow:#e9f1fb;
  --red:#c8161d;
  --ink:#111111;
  --white:#ffffff;
  --film:#1a1a1a;
  --grey:#555555;
  --brand:#1b4ea0;
}
*{margin:0;padding:0;box-sizing:border-box}
html,body{width:846px;height:1200px;overflow:hidden;background:var(--white)}
.poster{position:relative;width:846px;height:1200px;overflow:hidden;background:var(--white);font-family:"Noto Sans JP",sans-serif;color:var(--ink)}
.hero{position:absolute;left:0;top:0;width:846px;height:690px;
  background:linear-gradient(180deg,var(--sky-top) 0%,var(--sky-mid) 45%,#9cc1e8 72%,var(--snow) 100%)}
.film-strip{position:absolute;left:30px;top:0;width:140px;height:690px;background:var(--film);transform:rotate(-2deg);transform-origin:top left}
.film-strip .holes{position:absolute;top:0;bottom:0;width:10px;
  background:repeating-linear-gradient(180deg,var(--white) 0 8px,transparent 8px 18px)}
.film-strip .holes.left{left:6px}
.film-strip .holes.right{right:6px}
.film-frame{position:absolute;left:22px;width:96px;height:118px;background:linear-gradient(160deg,#6e93c4,#d8e4f2 60%,#8a6a52)}
.brand{position:absolute;left:14px;top:14px;z-index:2;display:flex;align-items:center;gap:8px;background:var(--white);padding:5px 12px;font-weight:900;font-size:24px;line-height:1.2;color:var(--brand)}
.brand i{display:block;width:16px;height:16px;border-radius:50%;background:var(--brand)}
.org-line{position:absolute;right:22px;top:26px;writing-mode:vertical-rl;font-family:"Noto Serif JP",serif;font-weight:700;font-size:17px;color:var(--white);letter-spacing:2px}
.title{position:absolute;left:600px;top:70px;writing-mode:vertical-rl;font-family:"Yuji Mai",serif;font-size:110px;line-height:1;color:var(--red);
  text-shadow:0 0 6px var(--white),0 0 12px var(--white),0 0 3px var(--white)}
.subtitle{position:absolute;left:548px;top:150px;writing-mode:vertical-rl;font-family:"Noto Serif JP",serif;font-weight:700;font-size:26px;color:var(--white);letter-spacing:4px;text-shadow:0 0 4px rgba(0,0,0,.5)}
.lead{position:absolute;left:370px;top:160px;height:330px;writing-mode:vertical-rl;font-family:"Noto Serif JP",serif;font-size:14px;line-height:1.9;color:var(--white);text-shadow:0 0 3px rgba(0,0,0,.6)}
.credit{position:absolute;right:18px;top:650px;font-size:10px;color:var(--white)}
.event-title{position:absolute;left:14px;top:700px;font-weight:900;font-size:78px;letter-spacing:-1px;line-height:1;white-space:nowrap}
.event-title .accent{color:var(--red)}
.speaker{position:absolute;left:20px;top:792px;font-weight:700;font-size:16px;line-height:1.4}
.speaker b{font-size:20px}
.free-box{position:absolute;left:0;top:832px;width:66px;height:276px;background:var(--red);color:var(--white);
  display:flex;align-items:center;justify-content:center}
.free-box span{writing-mode:vertical-rl;font-weight:900;font-size:44px;letter-spacing:6px}
.info{position:absolute;left:82px;top:842px;width:456px}
.info-row{display:flex;align-items:flex-start;gap:12px;margin-bottom:28px}
.info-label{flex:none;background:var(--red);color:var(--white);font-size:15px;font-weight:700;padding:4px 8px}
.date{font-weight:900;font-size:33px;line-height:1;white-space:nowrap}
.time{font-weight:700;font-size:20px;margin-top:10px}
.venue{font-weight:900;font-size:27px;line-height:1.1;white-space:nowrap}
.address{font-size:13px;margin-top:6px;color:var(--grey)}
.speaker-photo{position:absolute;left:540px;top:700px;width:306px;height:415px;background:linear-gradient(180deg,#d9dde3,#8a9099 55%,#1d2230)}
.apply-bar{position:absolute;left:0;top:1115px;width:846px;height:26px;background:var(--red);color:var(--white);display:flex;align-items:center;padding-left:20px;font-weight:700;font-size:15px;letter-spacing:2px}
.apply-text{position:absolute;left:20px;top:1148px;width:810px;font-size:12px;line-height:1.7}
</style>
</head>
<body>
<div class="poster">
  <div class="hero" role="img" aria-label="雪山の稜線を登る登山家の写真、青空と雪の斜面"></div>

  <div class="film-strip">
    <div class="holes left"></div><div class="holes right"></div>
    <div class="film-frame" style="top:10px" role="img" aria-label="雪山の山頂の写真"></div>
    <div class="film-frame" style="top:145px" role="img" aria-label="防寒具姿の登山家の写真"></div>
    <div class="film-frame" style="top:280px" role="img" aria-label="岩壁を登る登山家の写真"></div>
    <div class="film-frame" style="top:415px" role="img" aria-label="仲間との集合写真"></div>
    <div class="film-frame" style="top:550px" role="img" aria-label="山頂で笑顔の登山家の写真"></div>
  </div>

  <div class="brand"><i></i>PRV</div>

  <p class="org-line">青葉青年会議所 創立50周年記念講演会</p>
  <h1 class="title">仲間の絆</h1>
  <p class="subtitle">―夢と希望に向かって―</p>
  <p class="lead">世界の頂をめざす登山家が、<br>仲間と共に歩んだ道のり。<br>困難を越えて夢を追い続ける<br>ことの大切さを語ります。<br>ぜひ会場でその声を<br>お聞きください。</p>
  <p class="credit">写真提供:森川拓事務所</p>

  <h2 class="event-title">森川<span class="accent">拓</span>講演会</h2>
  <p class="speaker">講師 アルピニスト <b>森川拓氏</b></p>

  <div class="free-box"><span>入場無料</span></div>

  <div class="info">
    <div class="info-row">
      <span class="info-label">開催日時</span>
      <div><p class="date">平成25年7月14日(日)</p><p class="time">14:00〜16:30(開場13:00)</p></div>
    </div>
    <div class="info-row">
      <span class="info-label">開催会場</span>
      <div><p class="venue">青葉市北原市民会館 ホール</p><p class="address">青葉県青葉市北原町1-2-3 TEL 0123-45-6789</p></div>
    </div>
  </div>

  <div class="speaker-photo" role="img" aria-label="講師の上半身ポートレート写真"></div>

  <div class="apply-bar">講演会参加申込方法</div>
  <p class="apply-text">申込方法:往復はがきに氏名・住所・人数を記入のうえ事務局までお送りください。<br>問合せ:青葉青年会議所 事務局 受付 10:00〜17:00 TEL 0123-45-6789</p>
</div>
</body>
</html>
```